Hallo liebe Designer,
wir haben bereits ein Design, welches sich an den Farben unserer Homepage www.lorta.de orientiert. Dieses Design muss nachgebaut werden. Wir benötigen eine editierbare Microsoft-WORD-Datei, die nach Bedarf angepasst werden kann (falls sich Telefonnummer oder ähnliches mal ändert)
Zusammengefasst:
Benötigt wird: Ein Worddokument mit einem Briefpapier mit der Hauptseite und Folgeseiten. Die Folgeseiten sollen automatisch entstehen, wenn mehr wie 1 Seite beschrieben wird.
Das Design bitte so nachbauen wie es im PDF ersichtlich ist.
- das Worddokument muss anpassbar sein, falls sich mal die Telefonnummer o.ä. ändert

```html
<!DOCTYPE html>
<html lang="de">
<head>
<meta charset="utf-8">
<title>LOR Briefpapier</title>
<link rel="stylesheet" href="https://fonts.googleapis.com/css2?family=Arimo&family=Jost:wght@400&family=Hind:wght@600&display=swap">
<style>
:root{
  --backdrop:#a9a8ac;
  --paper:#ffffff;
  --ink:#111111;
  --muted:#8d8d8d;
  --brand:#9aa39b;
  --band-light:#a3a9a0;
  --band-dark:#7b817b;
  --rule:#8e948e;
}
*{margin:0;padding:0;box-sizing:border-box}
html,body{width:1200px;height:1200px;overflow:hidden;background:var(--backdrop)}
.letter{position:absolute;left:211px;top:50px;width:777px;height:1100px;background:var(--paper);overflow:hidden}
.brand{position:absolute;left:520px;top:70px;display:flex;align-items:center;gap:10px;font-family:"Hind",sans-serif;font-weight:600;color:var(--brand);font-size:22px;letter-spacing:.2px}
.brand-dot{width:16px;height:16px;border-radius:50%;background:var(--brand)}
.sender{position:absolute;left:56px;top:198px;font-family:"Jost",sans-serif;font-size:7px;color:var(--muted)}
.body-text{font-family:"Arimo",Arial,sans-serif;font-size:12.6px;color:var(--ink);line-height:18.2px}
.recipient{position:absolute;left:56px;top:241px;line-height:16.3px}
.recipient .city{margin-top:16px}
.subject{position:absolute;left:56px;top:401px}
.salutation{position:absolute;left:56px;top:438px}
.paragraph{position:absolute;left:56px;width:666px;text-align:justify;text-align-last:left}
.p1{top:475px}.p2{top:566px}.p3{top:658px}
.closing{position:absolute;left:56px;top:822px}
.footer-col{position:absolute;top:988px;font-family:"Jost",sans-serif;font-size:9.4px;line-height:12.5px;color:var(--muted)}
.col-management{left:56px}
.col-tax{left:209px}
.col-post{left:423px}
.contact-row{display:flex;align-items:center;gap:10px}
.contact-row svg{width:8px;height:8px}
.footer-rule{position:absolute;top:986px;width:1.5px;height:69px;background:var(--rule)}
.rule-1{left:193px}.rule-2{left:406px}
.footer-bands{position:absolute;left:0;top:1040px;width:777px;height:60px}
.web{position:absolute;left:614px;top:1057px;font-family:"Jost",sans-serif;font-size:17px;color:#fff}
</style>
</head>
<body>
<main class="letter">
  <div class="brand"><span class="brand-dot"></span>LOR Unternehmensgruppe</div>

  <p class="sender">LOR Unternehmensgruppe GmbH, Lindenallee 18, 61234 Ahornfeld</p>

  <address class="recipient body-text" style="font-style:normal">
    Musterfirma<br>z. Hd. Herrn Mustermann<br>Musterstraße 00
    <div class="city">01234 Musterstadt</div>
  </address>

  <p class="subject body-text">Betreffzeile</p>
  <p class="salutation body-text">Sehr geehrte Damen und Herren,</p>

  <p class="paragraph p1 body-text">Sehr geehrter Herr Mustermann, jeder Setzer hat für diesen Zweck immer etwas Blindtext parat. Blindtext ist im Umfang von einigen tausend Anschlägen, der für die »äußerliche« Gestaltung einer Publikation verwendet und dessen Inhalt unwichtig ist. Man setzt ihn oft zum Beispiel in verschiedenen Schriften und Schriftgrößen, um anderen zu zeigen, wie eine bestimmte Schrift wirkt.</p>
  <p class="paragraph p2 body-text">Sehr geehrter Herr Mustermann, jeder Setzer hat für diesen Zweck immer etwas Blindtext parat. Blindtext ist im Umfang von einigen tausend Anschlägen, der für die »äußerliche« Gestaltung einer Publikation verwendet und dessen Inhalt unwichtig ist. Man setzt ihn oft zum Beispiel in verschiedenen Schriften und Schriftgrößen, um anderen zu zeigen, wie eine bestimmte Schrift wirkt.</p>
  <p class="paragraph p3 body-text">Sehr geehrter Herr Mustermann, jeder Setzer hat für diesen Zweck immer etwas Blindtext parat. Blindtext ist im Umfang von einigen tausend Anschlägen, der für die »äußerliche« Gestaltung einer Publikation verwendet und dessen Inhalt unwichtig ist. Man setzt ihn oft zum Beispiel in verschiedenen Schriften und Schriftgrößen, um anderen zu zeigen, wie eine bestimmte Schrift wirkt.</p>

  <p class="closing body-text">Mit freundlichen Grüßen</p>

  <div class="footer-col col-management">Geschäftsführung:<br>Markus Helbig<br>Karina Wendt<br>Amtsgericht Ahornfeld<br>HRB 10000</div>
  <span class="footer-rule rule-1"></span>
  <div class="footer-col col-tax">Umsatzsteuer-ID<br>DE000123456<br>Sparkasse Birkental<br>BIC: BIRKDEXXXXX<br>IBAN: DE00 1234 5678 9012 3456 78</div>
  <span class="footer-rule rule-2"></span>
  <div class="footer-col col-post">Postanschrift:<br>Eschenweg 7<br>45678 Birkental
    <div class="contact-row"><svg viewBox="0 0 10 10"><path d="M2 0.5l2 2-1 1.2c.6 1.3 1.6 2.3 2.9 2.9l1.2-1 2 2-1.3 1.6C4 9 1 6 0.5 1.8z" fill="#8d8d8d"/></svg><span>&nbsp;+49 123 / 45678900</span></div>
    <div class="contact-row"><svg viewBox="0 0 10 10"><rect x=".5" y="1.5" width="9" height="7" fill="none" stroke="#8d8d8d"/><path d="M.5 1.5l4.5 4 4.5-4" fill="none" stroke="#8d8d8d"/></svg><span>&nbsp;info@lorta.de</span></div>
  </div>

  <svg class="footer-bands" viewBox="0 0 777 60" preserveAspectRatio="none" aria-hidden="true">
    <rect x="0" y="31" width="777" height="29" fill="var(--band-light)"/>
    <polygon points="552,3 777,3 777,60 515,60" fill="var(--band-dark)"/>
  </svg>
  <span class="web">www.lorta.de</span>
</main>
</body>
</html>
```